Prepared Meal Delivery Website

Need a new modern design for a prepared meal delivery company that is hosted on Shopify.

Target Market(s)

Young Professionals

Industry/Entity Type

Prepared Meal Delivery Service

Number of Pages Required

5+ page

Requirements
Must have
• Use https://www.velmorafoods.com/ as an example
Nice to have
• Vibrant page with call to action obvious and repeated
Should not have
• Generic look, grays/white/black

```html
<!DOCTYPE html>
<html lang="en">
<head>
<meta charset="utf-8">
<title>Fleet Fork Meals – Prepared Meal Delivery Service</title>
<link rel="stylesheet" href="https://fonts.googleapis.com/css2?family=Barlow+Condensed:wght@600;700&family=Overpass:wght@400;600&display=swap">
<style>
:root{
  --red:#d9381e;
  --orange:#f29a2e;
  --cream:#f3f1ec;
  --ink:#111111;
  --muted:#5b5b5b;
  --forest:#0f2b22;
  --white:#ffffff;
  --ghost:rgba(0,0,0,0.07);
}
*{box-sizing:border-box;margin:0;padding:0}
html,body{width:1200px;height:4882px;overflow:hidden}
body{position:relative;background:var(--white);font-family:"Overpass",Arial,sans-serif;color:var(--ink)}
.abs{position:absolute}
.head{font-family:"Barlow Condensed","Arial Narrow",sans-serif;font-weight:700;text-transform:uppercase;letter-spacing:.5px}
.btn{position:absolute;display:flex;align-items:center;justify-content:center;font-family:"Barlow Condensed","Arial Narrow",sans-serif;font-weight:700;text-transform:uppercase;text-decoration:none}
.photo{position:absolute}

/* header */
.nav-btn{left:19px;top:23px;width:148px;height:53px;background:var(--red);color:var(--white);font-size:18px;gap:10px}
.logo{position:absolute;left:528px;top:27px;width:144px;height:144px;border-radius:50%;background:var(--white);border:4px solid var(--ink);box-shadow:0 0 0 6px var(--white);display:flex;align-items:center;justify-content:center;text-align:center;z-index:3;font-family:"Barlow Condensed",sans-serif;font-weight:700;font-size:20px;line-height:1.05;text-transform:uppercase;color:var(--ink)}
.social{position:absolute;width:46px;height:46px;border-radius:50%;background:var(--orange)}
.shop-top{left:1031px;top:23px;width:146px;height:53px;border:3px solid var(--red);color:var(--red);font-size:18px}

/* hero */
.hero{left:19px;top:100px;width:1160px;height:583px;background:radial-gradient(ellipse at 30% 40%,#8a4a2c,#5a3a24 45%,#3b2a1c)}
.hero-shade{left:19px;top:100px;width:1160px;height:583px;background:rgba(0,0,0,.28)}
.hero-title{left:19px;width:1160px;text-align:center;color:var(--white);font-size:58px;line-height:1}
.hero-btn{left:525px;top:464px;width:148px;height:52px;border:4px solid var(--orange);color:var(--orange);font-size:13px}
.slide-mark{left:1062px;width:52px;height:5px;background:var(--orange)}

/* how it works */
.how{left:19px;top:707px;width:1160px;height:819px;background:var(--cream)}
.ghost{position:absolute;font-family:"Barlow Condensed",sans-serif;font-weight:700;text-transform:uppercase;color:var(--ghost);white-space:nowrap}
.how-title{left:85px;top:855px;font-size:52px;line-height:68px}
.step-icon{position:absolute;left:84px;width:62px;height:62px;border-radius:46% 54% 50% 50%}
.step-title{position:absolute;left:173px;font-family:"Barlow Condensed",sans-serif;font-weight:700;font-size:20px}
.step-text{position:absolute;left:173px;width:400px;font-size:13px;line-height:21px;color:var(--muted)}

/* plans */
.section-title{position:absolute;left:0;width:1200px;text-align:center;font-size:54px;line-height:1}
.plan{position:absolute;top:1765px;width:274px;height:377px}
.plan .price{position:absolute;left:25px;top:240px;background:var(--red);color:var(--white);font-family:"Barlow Condensed",sans-serif;font-weight:700;font-size:13px;padding:5px 10px}
.plan .name{position:absolute;left:25px;top:276px;color:var(--white);font-family:"Barlow Condensed",sans-serif;font-weight:700;font-size:28px}
.plan .add{position:absolute;left:25px;top:330px;color:var(--white);font-size:13px;display:flex;align-items:center;gap:8px}
.pager{top:2190px;width:154px;height:62px;background:var(--ink);color:var(--white);font-size:14px}

/* offer */
.offer{left:19px;top:2389px;width:1160px;height:758px;background:var(--cream)}
.offer-box{position:absolute;top:2637px;height:129px;border:4px solid var(--orange);text-align:center;padding:16px 14px 0}
.offer-box h3{font-family:"Barlow Condensed",sans-serif;font-weight:700;font-size:21px;margin-bottom:4px}
.offer-box p{font-size:13px;line-height:21px;color:var(--muted)}
.delivery-title{left:0;width:1200px;text-align:center;top:2822px;font-size:22px}
.delivery-sub{left:0;width:1200px;text-align:center;top:2858px;font-size:13px;color:var(--muted)}
.day{position:absolute;top:2905px;height:106px;background:var(--white);text-align:center;font-size:13px;color:#b4b4b4;padding-top:24px}
.day.on{border-top:5px solid var(--red);color:var(--red);padding-top:19px}
.day svg{display:block;margin:12px auto 0}

/* calorie */
.cal-photo{left:19px;top:3178px;width:567px;height:487px;background:linear-gradient(135deg,#e7b96a,#2f7f9c 55%,#2d6c4a)}
.cal-panel{left:612px;top:3178px;width:567px;height:487px;background:var(--red)}
.cal-title{left:685px;top:3270px;color:var(--white);font-size:54px;line-height:68px}
.cal-text{left:685px;top:3446px;width:370px;color:var(--white);font-size:13px;line-height:21px}
.cal-btn{left:685px;top:3530px;width:147px;height:53px;border:4px solid var(--white);color:var(--white);font-size:13px}

/* testimonial */
.quote-panel{left:85px;top:4067px;width:1028px;height:271px;background:var(--cream)}
.client-photo{left:764px;top:3902px;width:286px;height:345px;background:linear-gradient(160deg,#c9ccd0,#8e949a 60%,#6f7478)}
.client-name{left:450px;width:251px;text-align:right;top:4086px;font-family:"Barlow Condensed",sans-serif;font-weight:700;font-size:34px}
.client-text{left:200px;width:501px;text-align:right;top:4152px;font-size:13px;line-height:22px;color:#333}
.client-rule{left:470px;top:4230px;width:231px;height:2px;background:var(--red)}
.dot{position:absolute;top:4280px;width:11px;height:11px;border-radius:50%}

/* cta */
.cta-text{left:85px;top:4380px;font-family:"Barlow Condensed",sans-serif;font-weight:700;font-size:36px}
.cta-btn{left:967px;top:4376px;width:146px;height:55px;border:3px solid var(--red);color:var(--red);font-size:18px}

/* footer */
.footer{left:0;top:4474px;width:1200px;height:408px;background:var(--forest)}
.foot-logo{position:absolute;left:541px;top:4535px;width:118px;height:118px;border-radius:50%;border:3px solid var(--white);display:flex;align-items:center;justify-content:center;text-align:center;color:var(--white);font-family:"Barlow Condensed",sans-serif;font-weight:700;font-size:16px;line-height:1.05;text-transform:uppercase}
.foot-rule{left:85px;width:1028px;height:1px;background:rgba(255,255,255,.35)}
.foot-nav{left:0;width:1200px;top:4706px;display:flex;justify-content:center;gap:24px;color:var(--white);font-family:"Barlow Condensed",sans-serif;font-weight:700;font-size:14px;text-transform:uppercase}
.copyright{left:0;width:1200px;top:4768px;text-align:center;color:var(--white);font-size:13px}
.follow{left:505px;top:4803px;color:var(--white);font-family:"Barlow Condensed",sans-serif;font-weight:700;font-size:20px;text-transform:uppercase}
</style>
</head>
<body>

<!-- header -->
<a class="btn nav-btn" href="#"><svg width="16" height="14" viewBox="0 0 16 14"><path d="M0 1h16M0 7h16M0 13h16" stroke="#fff" stroke-width="2"/></svg>Navigation</a>
<div class="logo">Fleet Fork<br>Meals</div>
<span class="social" style="left:897px;top:24px"></span>
<span class="social" style="left:959px;top:24px"></span>
<a class="btn shop-top" href="#">Shop Meal Plan</a>

<!-- hero -->
<div class="photo hero" role="img" aria-label="Meal prep containers with chicken, vegetables and tomatoes on a wooden table"></div>
<div class="abs hero-shade"></div>
<div class="abs head hero-title" style="top:298px">Prepared</div>
<div class="abs head hero-title" style="top:376px">Meal Delivery Service</div>
<a class="btn hero-btn" href="#">See Meal Plans</a>
<span class="abs slide-mark" style="top:360px"></span>
<span class="abs slide-mark" style="top:390px;width:26px;left:1088px;background:var(--white)"></span>
<span class="abs slide-mark" style="top:412px;width:26px;left:1088px;background:var(--white)"></span>

<!-- how it works -->
<section class="abs how"></section>
<div class="ghost" style="left:85px;top:830px;font-size:80px;line-height:76px">Fleet Fork<br>Meals</div>
<h2 class="abs head how-title">How Fleet Fork Meals<br>Plan Works</h2>

<div class="step-icon" style="top:1050px;background:#f6d8c8"><svg width="62" height="62"><circle cx="31" cy="33" r="13" fill="none" stroke="#e4643e" stroke-width="2"/><path d="M16 44h30" stroke="#e4643e" stroke-width="2"/></svg></div>
<div class="step-title" style="top:1048px">Pick your Meal Plan</div>
<p class="step-text" style="top:1080px">Lorem ipsum dolor sit amet, consectetur adipiscing elit. Etiam ornare molestie tellus. Vivamus auctor ligula eu lorem sodales consectetur. Duis velit mi</p>

<div class="step-icon" style="top:1175px;background:#d5ecd8"><svg width="62" height="62"><rect x="20" y="20" width="22" height="22" rx="4" fill="none" stroke="#3f9b59" stroke-width="2"/><path d="M25 31h12" stroke="#3f9b59" stroke-width="2"/></svg></div>
<div class="step-title" style="top:1172px">We Do The Coaching</div>
<p class="step-text" style="top:1204px">Lorem ipsum dolor sit amet, consectetur adipiscing elit. Etiam ornare molestie tellus. Vivamus auctor ligula eu lorem sodales consectetur. Duis velit mi</p>

<div class="step-icon" style="top:1300px;background:#dcdaf3"><svg width="62" height="62"><circle cx="31" cy="31" r="12" fill="none" stroke="#5e57c7" stroke-width="2"/><path d="M31 22v18M22 31h18" stroke="#5e57c7" stroke-width="2"/></svg></div>
<div class="step-title" style="top:1298px">We Do The Coaching</div>
<p class="step-text" style="top:1330px">Lorem ipsum dolor sit amet, consectetur adipiscing elit. Etiam ornare molestie tellus. Vivamus auctor ligula eu lorem sodales consectetur. Duis velit mi</p>

<div class="photo" style="left:641px;top:973px;width:252px;height:341px;background:linear-gradient(160deg,#9fb3c2,#8a5a5a 55%,#6b7a4a)" role="img" aria-label="Hands packing meal prep containers"></div>
<div class="photo" style="left:921px;top:859px;width:192px;height:244px;background:linear-gradient(180deg,#3a3a3a,#232323 60%,#6b5a2a)" role="img" aria-label="Black meal box with rice and vegetables on slate"></div>
<div class="photo" style="left:921px;top:1145px;width:192px;height:245px;background:linear-gradient(160deg,#c8d6dc,#d9c38a 50%,#7e9a6a)" role="img" aria-label="Rows of salad meal containers being prepared"></div>

<!-- plans -->
<div class="ghost" style="left:0;width:1200px;text-align:center;top:1655px;font-size:84px">Fleet Fork Meals</div>
<h2 class="head section-title" style="top:1672px">Choose Your Plan</h2>

<article class="plan" style="left:19px;background:linear-gradient(180deg,#3b3b3b,#6a6a5a 55%,#2a2a2a)" role="img" aria-label="Plated clean meal with greens">
  <span class="price">$110.99 / Week</span><span class="name">Clean Meal Plan</span>
  <span class="add">Add To Order <svg width="20" height="8"><path d="M0 4h18M14 1l4 3-4 3" stroke="#fff" fill="none" stroke-width="1.5"/></svg></span>
</article>
<article class="plan" style="left:318px;background:linear-gradient(180deg,#c9c9c9,#9a6a4a 50%,#3a2a20)" role="img" aria-label="Paleo meal containers">
  <span class="price">$110.99 / Week</span><span class="name">Paleo Meal Plan</span>
  <span class="add">Add To Order <svg width="20" height="8"><path d="M0 4h18M14 1l4 3-4 3" stroke="#fff" fill="none" stroke-width="1.5"/></svg></span>
</article>
<article class="plan" style="left:609px;background:linear-gradient(180deg,#6a8a5a,#5a7a4a 50%,#2a3a22)" role="img" aria-label="Salad meal containers">
  <span class="price">$110.99 / Week</span><span class="name">Approved Meal Plan</span>
  <span class="add">Add To Order <svg width="20" height="8"><path d="M0 4h18M14 1l4 3-4 3" stroke="#fff" fill="none" stroke-width="1.5"/></svg></span>
</article>
<article class="plan" style="left:908px;background:linear-gradient(180deg,#2a2a2a,#8a8a8a 50%,#2a2a2a)" role="img" aria-label="Chef preparing keto meals">
  <span class="price">$110.99 / Week</span><span class="name">Keto Meal Plan</span>
  <span class="add">Add To Order <svg width="20" height="8"><path d="M0 4h18M14 1l4 3-4 3" stroke="#fff" fill="none" stroke-width="1.5"/></svg></span>
</article>
<a class="btn pager" href="#" style="left:444px">Prev</a>
<a class="btn pager" href="#" style="left:601px">Next</a>

<!-- offer -->
<section class="abs offer"></section>
<div class="ghost" style="left:0;width:1200px;text-align:center;top:2515px;font-size:84px">Fleet Fork Meals</div>
<h2 class="head section-title" style="top:2532px">What We Offer</h2>
<div class="offer-box" style="left:85px;width:237px"><h3>Various Duration</h3><p>Shop 9 different meal plan subscriptions build for the taste and results</p></div>
<div class="offer-box" style="left:351px;width:235px"><h3>Health Diet</h3><p>Shop 9 different meal plan subscriptions build for the taste and results</p></div>
<div class="offer-box" style="left:612px;width:236px"><h3>Personal Account</h3><p>Shop 9 different meal plan subscriptions build for the taste and results</p></div>
<div class="offer-box" style="left:876px;width:235px"><h3>Trial Week</h3><p>Shop 9 different meal plan subscriptions build for the taste and results</p></div>
<div class="abs head delivery-title">Free On-Time Delivary</div>
<p class="abs delivery-sub">From 6 am to 12 pm ,you can choose time interval and schedule suitable for you.</p>

<div class="day" style="left:228px;width:89px">SUN</div>
<div class="day on" style="left:336px;width:87px">MON<svg width="22" height="24"><rect x="1" y="7" width="20" height="16" rx="2" fill="#a8a8a8"/><path d="M6 8V5a5 5 0 0110 0v3" stroke="#a8a8a8" stroke-width="2" fill="none"/></svg></div>
<div class="day" style="left:442px;width:89px">TUE</div>
<div class="day on" style="left:550px;width:87px">WED<svg width="22" height="24"><rect x="1" y="7" width="20" height="16" rx="2" fill="#a8a8a8"/><path d="M6 8V5a5 5 0 0110 0v3" stroke="#a8a8a8" stroke-width="2" fill="none"/></svg></div>
<div class="day" style="left:658px;width:89px">THR</div>
<div class="day on" style="left:768px;width:87px">FRI<svg width="22" height="24"><rect x="1" y="7" width="20" height="16" rx="2" fill="#a8a8a8"/><path d="M6 8V5a5 5 0 0110 0v3" stroke="#a8a8a8" stroke-width="2" fill="none"/></svg></div>
<div class="day on" style="left:876px;width:89px">SAT<svg width="22" height="24"><rect x="1" y="7" width="20" height="16" rx="2" fill="#a8a8a8"/><path d="M6 8V5a5 5 0 0110 0v3" stroke="#a8a8a8" stroke-width="2" fill="none"/></svg></div>

<!-- calorie -->
<div class="photo cal-photo" role="img" aria-label="Hand holding a phone with a calorie tracker between donuts, chips and fresh vegetables"></div>
<section class="abs cal-panel"></section>
<div class="ghost" style="left:800px;top:3262px;font-size:80px;line-height:76px;color:rgba(255,255,255,.12)">Fleet Fork<br>Meals</div>
<h2 class="abs head cal-title">Calorie<br>Calculator</h2>
<p class="abs cal-text">Lorem ipsum dolor sit amet, consectetur adipiscing elit. Etiam ornare molestie tellus. Vivamus auctor ligula eu lorem sodales consectetur. Duis velit mi</p>
<a class="btn cal-btn" href="#">Calculate</a>

<!-- testimonial -->
<div class="ghost" style="left:0;width:1200px;text-align:center;top:3795px;font-size:84px">Fleet Fork Meals</div>
<h2 class="head section-title" style="top:3812px">What Our Client Say</h2>
<section class="abs quote-panel"></section>
<div class="photo client-photo" role="img" aria-label="Smiling client in a white t-shirt holding a tablet in a gym"></div>
<svg class="abs" style="left:148px;top:4060px" width="50" height="40" viewBox="0 0 50 40"><path d="M2 38V20C2 9 8 3 18 1l2 5c-6 2-9 6-9 11h9v21zM28 38V20c0-11 6-17 16-19l2 5c-6 2-9 6-9 11h9v21z" fill="#f1a08e"/></svg>
<div class="abs client-name">Jhon Doe</div>
<p class="abs client-text">Lorem ipsum dolor sit amet, consectetur adipiscing elit. Etiam ornare molestie tellus. Vivamus auctor ligula eu lorem sodales consectetur. Duis velit mi, imperdiet vel tincidunt a, cursus non magna.</p>
<span class="abs client-rule"></span>
<span class="dot" style="left:649px;background:var(--red)"></span>
<span class="dot" style="left:669px;background:#f1a08e"></span>
<span class="dot" style="left:689px;background:#f1a08e"></span>

<!-- cta -->
<div class="abs cta-text">Begin your new healthy life with us today</div>
<a class="btn cta-btn" href="#">Shop Meal Plan</a>

<!-- footer -->
<footer class="abs footer"></footer>
<div class="foot-logo">Fleet Fork<br>Meals</div>
<span class="abs foot-rule" style="top:4689px"></span>
<nav class="abs foot-nav"><span>About</span><span>Meal Plans</span><span>How It Works</span><span>Testimonials</span><span>Contact</span></nav>
<span class="abs foot-rule" style="top:4740px"></span>
<p class="abs copyright">Copyright 2022,Fleet Fork Meals.All right reserved.</p>
<div class="abs follow">Follow Us</div>
<span class="social" style="left:604px;top:4800px;width:38px;height:38px"></span>
<span class="social" style="left:656px;top:4800px;width:38px;height:38px"></span>

</body>
</html>
```